Refresh web site from year 2003

Voltaro Works has a web site (https://vowrk-site.no/) from early 2000 that needs to be refreshed.

Attached are company logo, favicon files, a licensed image to be used, an animation that illustrate the use of one of the products.

Target Market(s)

Industrial customers

Industry/Entity Type

Electrical Switch Board Builders, Automation Industry

Coding

Coded - Design and coding required

Number of Pages Required

3 page

Requirements
Must have
• WordPress site. Use attached animation in the front page (source file is in Adobe Animation format, if adjustments are needed). Product page for two products, "KTR" and "QX-7 Ver B".
Nice to have
• The site should focus on promoting two products KTR and QX-7 Ver B.

```html
<!DOCTYPE html>
<html lang="en">
<head>
<meta charset="utf-8">
<title>Voltaro Works</title>
<link href="https://fonts.googleapis.com/css2?family=Berkshire+Swash&family=Roboto:wght@400;500;700&display=swap" rel="stylesheet">
<style>
:root{
  --blue:#0d4a8c;
  --blue-dark:#0a3a70;
  --ink:#222;
  --muted:#555;
  --card:#e9ebf0;
  --gold:#e0a400;
  --footer:#1e1f22;
  --line:#8a8a8a;
}
*{box-sizing:border-box;margin:0;padding:0}
html,body{width:1200px;height:3745px;overflow:hidden}
body{position:relative;font-family:'Roboto',Arial,sans-serif;color:var(--ink);background:#fff}
.abs{position:absolute}
.display{font-family:'Berkshire Swash',Georgia,serif;font-weight:400}
.btn{position:absolute;display:flex;align-items:center;justify-content:center;background:var(--blue);color:#fff;border-radius:3px;font-family:'Berkshire Swash',Georgia,serif;font-size:15px}

/* hero */
.hero{position:absolute;left:0;top:0;width:1200px;height:643px}
.hero-photo{position:absolute;inset:0;background:linear-gradient(160deg,#c0792f 0%,#7a4a36 22%,#2b3a5c 50%,#1d2b45 75%,#2f3f58 100%)}
.hero-shade{position:absolute;inset:0;background:rgba(10,20,40,.35)}
.brand{position:absolute;display:flex;align-items:center;gap:10px;color:#fff;font-family:'Roboto',Arial,sans-serif;font-weight:700;font-size:22px;white-space:nowrap}
.brand-mark{width:14px;height:14px;border-radius:50%;background:#fff}
.nav a{position:absolute;top:57px;color:#fff;font-size:15px;text-decoration:none}
.hero-title{position:absolute;left:0;width:1200px;top:280px;text-align:center;color:#fff;font-size:42px}
.hero-text{position:absolute;left:330px;width:540px;top:342px;text-align:center;color:#fff;font-size:15px;line-height:26px}
.arrow{position:absolute;top:304px;width:36px;height:36px;border-radius:50%;background:#fff}

/* about */
.eyebrow{position:absolute;left:111px;top:724px;font-family:'Berkshire Swash',Georgia,serif;font-size:11px;color:#333}
.eyebrow::before{content:"";display:inline-block;width:36px;height:2px;background:var(--blue);vertical-align:middle;margin-right:10px}
.about-title{position:absolute;left:111px;top:752px;font-size:23px;line-height:31px;color:var(--blue);white-space:nowrap}
.about-text{position:absolute;left:630px;width:458px;top:724px;font-size:15px;line-height:27.5px;color:#444;text-align:justify}
.about-text p+p{margin-top:13px}

/* products */
.products{position:absolute;left:0;top:1251px;width:1200px;height:740px;background:linear-gradient(180deg,#0f4a8a,#0d4584 60%,#0c3f7a)}
.vline{position:absolute;left:599px;width:2px;height:40px}
.sec-title{position:absolute;left:0;width:1200px;text-align:center;font-size:30px}
.tabs{position:absolute;left:352px;top:1376px;display:flex;border:2px solid #fff}
.tabs span{width:124px;height:46px;display:flex;align-items:center;justify-content:center;color:#fff;font-family:'Berkshire Swash',Georgia,serif;font-size:17px;border-left:2px solid #fff}
.tabs span:first-child{border-left:0;background:#fff;color:var(--blue)}
.pcard{position:absolute;top:1482px;width:231px;height:344px;background:var(--card)}
.pcard .ph{position:absolute;left:8px;top:8px;width:215px;height:162px;background:linear-gradient(180deg,#dcdde0,#cfd0d4)}
.pcard h3{position:absolute;left:0;width:231px;top:192px;text-align:center;color:var(--blue);font-family:'Berkshire Swash',Georgia,serif;font-size:14px;font-weight:400}
.pcard p{position:absolute;left:0;width:231px;top:223px;text-align:center;font-size:13px;color:#333}
.pcard .stars{position:absolute;left:0;width:231px;top:246px;text-align:center;color:var(--gold);font-size:14px;letter-spacing:3px}
.pcard .btn{left:50px;top:283px;width:110px;height:37px;font-size:13px}

/* services */
.services{position:absolute;left:0;top:1991px;width:1200px;height:802px;background:linear-gradient(180deg,#e5e8ee,#d8dde6 50%,#e3e5ea)}
.scard{position:absolute;top:2165px;width:315px;height:462px;background:#fff;box-shadow:0 2px 10px rgba(0,0,0,.08)}
.scard .ph{position:absolute;left:0;top:0;width:315px;height:220px}
.scard .icon{position:absolute;left:113px;top:175px;width:88px;height:88px;border-radius:50%;background:var(--blue);border:4px solid #fff;display:flex;align-items:center;justify-content:center}
.scard h3{position:absolute;left:0;width:315px;top:278px;text-align:center;color:var(--blue);font-family:'Berkshire Swash',Georgia,serif;font-size:20px;font-weight:400}
.scard p{position:absolute;left:30px;width:255px;top:317px;text-align:center;font-size:14.5px;line-height:24px;color:#444}
.scard .btn{left:102px;top:383px;width:110px;height:38px;font-size:13px}

/* contact */
.field label{position:absolute;font-size:17px;font-weight:500;color:#111}
.field .val{position:absolute;font-size:15px;color:#333}
.field .rule{position:absolute;height:1px;background:var(--line)}

/* footer */
.footer{position:absolute;left:0;top:3395px;width:1200px;height:350px;background:var(--footer);color:#fff}
.fhead{position:absolute;font-family:'Berkshire Swash',Georgia,serif;font-size:17px;color:#fff}
.flist{position:absolute;list-style:none;font-size:15px;line-height:32px;color:#fff}
.social{position:absolute;top:3625px;width:31px;height:31px;border-radius:50%;border:1.5px solid #fff}
</style>
</head>
<body>

<!-- hero -->
<section class="hero">
  <div class="hero-photo" role="img" aria-label="Technician in hard hat wiring an industrial switchboard cabinet"></div>
  <div class="hero-shade"></div>
</section>
<div class="brand" style="left:111px;top:50px"><span class="brand-mark"></span>Voltaro Works</div>
<nav class="nav">
  <a style="left:416px">Home</a>
  <a style="left:492px">About</a>
  <a style="left:567px">Services</a>
  <a style="left:660px">Products</a>
  <a style="left:757px">Contact</a>
</nav>
<svg class="abs" style="left:843px;top:58px" width="16" height="16" viewBox="0 0 16 16"><circle cx="6.5" cy="6.5" r="4.5" fill="none" stroke="#fff" stroke-width="2.2"/><line x1="10" y1="10" x2="14" y2="14" stroke="#fff" stroke-width="2.4"/></svg>
<div class="btn" style="left:895px;top:45px;width:98px;height:40px">Log in</div>
<div class="abs" style="left:1031px;top:57px;color:#fff;font-size:13px;font-weight:700">EN</div>
<svg class="abs" style="left:1049px;top:60px" width="11" height="8" viewBox="0 0 11 8"><path d="M1 1l4.5 5L10 1" fill="none" stroke="#fff" stroke-width="2"/></svg>
<svg class="abs" style="left:1068px;top:56px" width="18" height="18" viewBox="0 0 18 18" fill="none" stroke="#fff" stroke-width="1.4"><circle cx="9" cy="9" r="7.5"/><ellipse cx="9" cy="9" rx="3.5" ry="7.5"/><line x1="1.5" y1="9" x2="16.5" y2="9"/></svg>

<h1 class="hero-title display">Welcome to Voltaro Works</h1>
<p class="hero-text">Our business idea is to contribute with good and cost-effective electronics products for the industrial market, as well as seek and further develop</p>
<div class="btn" style="left:530px;top:408px;width:140px;height:42px">Get Started</div>
<div class="arrow" style="left:40px"><svg width="36" height="36" viewBox="0 0 36 36"><path d="M20 12l-6 6 6 6" fill="none" stroke="var(--blue)" stroke-width="3"/></svg></div>
<div class="arrow" style="left:1130px"><svg width="36" height="36" viewBox="0 0 36 36"><path d="M16 12l6 6-6 6" fill="none" stroke="var(--blue)" stroke-width="3"/></svg></div>

<!-- about -->
<div class="eyebrow">ABOUT US</div>
<h2 class="about-title display">LOREM IPSUM DOLOR SIT AMET,<br>CONSECTETUR ADIPISCING</h2>
<div class="abs" style="left:0;top:862px;width:276px;height:302px;background:var(--blue)"></div>
<div role="img" aria-label="Row of industrial switchboard cabinets with meters and breakers" class="abs" style="left:219px;top:830px;width:373px;height:302px;background:linear-gradient(90deg,#8b8f94,#d9dadc 45%,#bfc3c6 70%,#8e9296)"></div>
<div class="about-text">
  <p>Voltaro Works is a production and development company for electronics with an emphasis on small series production. We are currently 2 employees with good and relevant access to extra expertise in the established network. The company was established in 1985 and has since 2001 taken over production equipment and production basis from another company in the same industry.</p>
  <p>Sed ut perspiciatis unde omnis iste natus error sit voluptatem accusantium doloremque laudantium, totam rem aperiam, eaque ipsa quae ab illo inventore veritatis et quasi architecto beatae vitae dicta sunt explicabo. Nemo enim ipsam voluptatem quia voluptas sit aspernatur aut odit aut fugit, sed quia consequuntur magni dolores eos qui ratione voluptatem sequi nesciunt.</p>
</div>
<div class="btn" style="left:630px;top:1085px;width:140px;height:45px">Read more</div>

<!-- products -->
<section class="products"></section>
<div class="vline" style="top:1251px;background:#fff"></div>
<h2 class="sec-title display" style="top:1304px;color:#fff">Our Product</h2>
<div class="tabs"><span>ALL</span><span>LCD</span><span>LED</span><span>RELAY</span></div>

<article class="pcard" style="left:111px">
  <div class="ph" role="img" aria-label="Signal lamp product photo"></div>
  <h3>Signallampe</h3><p>med innebygget LED pære</p><div class="stars">★★★★★</div>
  <div class="btn">Buy now</div>
</article>
<article class="pcard" style="left:359px">
  <div class="ph" role="img" aria-label="Panel instrument gauge product photo"></div>
  <h3>Panel Instruments</h3><p>Leveres i LCD og LED</p><div class="stars">★★★★★</div>
  <div class="btn">Buy now</div>
</article>
<article class="pcard" style="left:608px">
  <div class="ph" role="img" aria-label="Minimum voltage relay module product photo"></div>
  <h3>Minimum Voltage Relay</h3><p>Relay type QX-7 against</p><div class="stars">★★★★★</div>
  <div class="btn">Buy now</div>
</article>
<article class="pcard" style="left:857px">
  <div class="ph" role="img" aria-label="Switch position indicator product photo"></div>
  <h3>Switch Position</h3><p>indicators Indicators with</p><div class="stars">★★★★★</div>
  <div class="btn">Buy now</div>
</article>

<!-- services -->
<section class="services"></section>
<div class="vline" style="top:1991px;background:var(--blue)"></div>
<h2 class="sec-title display" style="top:2071px;color:var(--blue)">Our Services</h2>

<article class="scard" style="left:112px">
  <div class="ph" role="img" aria-label="Gloved hands testing wiring in a control panel" style="background:linear-gradient(135deg,#c9c7b8,#8f9aa8 55%,#5e6d86)"></div>
  <div class="icon"><svg width="44" height="44" viewBox="0 0 44 44" fill="none" stroke="#fff" stroke-width="2"><circle cx="22" cy="16" r="10"/><path d="M22 16l5-4"/><path d="M22 26v6M10 34h24v5H10z"/></svg></div>
  <h3>Pressure Calculator</h3>
  <p>Conversion table for the 9 most common pressure units</p>
  <div class="btn">Read more</div>
</article>
<article class="scard" style="left:443px">
  <div class="ph" role="img" aria-label="Open electrical cabinet with dense wiring and terminals" style="background:linear-gradient(135deg,#9aa3ad,#5f6f80 50%,#3e5068)"></div>
  <div class="icon"><svg width="44" height="44" viewBox="0 0 44 44" fill="none" stroke="#fff" stroke-width="2"><circle cx="22" cy="22" r="15"/><circle cx="22" cy="22" r="9"/><path d="M22 16l5 3v6l-5 3-5-3v-6z"/></svg></div>
  <h3>Production</h3>
  <p>Small series production of electronics units in the number of 10 to 200 units.</p>
  <div class="btn">Read more</div>
</article>
<article class="scard" style="left:773px">
  <div class="ph" role="img" aria-label="Pre-assembled circuit boards and switch panels" style="background:linear-gradient(90deg,#dfe0e2,#b9bcc0 50%,#e2e3e5)"></div>
  <div class="icon"><svg width="44" height="44" viewBox="0 0 44 44" fill="none" stroke="#fff" stroke-width="2"><path d="M10 8h16l6 6v22H10z"/><path d="M16 20l6-3 6 3v7l-6 3-6-3z"/><path d="M30 30l6 6"/></svg></div>
  <h3>Design</h3>
  <p>Designing of electronics and printed circuit boards for pre-assembled and</p>
  <div class="btn">Read more</div>
</article>

<!-- contact -->
<div class="vline" style="top:2793px;background:var(--blue)"></div>
<h2 class="sec-title display" style="top:2870px;color:var(--blue)">Contact Us</h2>
<form>
  <div class="field"><label style="left:147px;top:2955px">Name</label><span class="val" style="left:147px;top:2986px">| Frist name</span><div class="rule" style="left:144px;top:3014px;width:384px"></div></div>
  <div class="field"><label style="left:651px;top:2955px">Email Address</label><span class="val" style="left:651px;top:2986px">@anymail.com</span><div class="rule" style="left:649px;top:3014px;width:384px"></div></div>
  <div class="field"><label style="left:147px;top:3060px">Phone</label><span class="val" style="left:147px;top:3090px">+1 888 888 8888</span><div class="rule" style="left:144px;top:3119px;width:384px"></div></div>
  <div class="field"><label style="left:654px;top:3060px">Company</label><span class="val" style="left:654px;top:3090px">Lorem ipsum</span><div class="rule" style="left:652px;top:3119px;width:384px"></div></div>
  <div class="field"><label style="left:147px;top:3180px">Comments</label><span class="val" style="left:147px;top:3213px">Lorem ipsum dolor</span><div class="rule" style="left:144px;top:3248px;width:911px"></div></div>
  <div class="btn" style="left:535px;top:3282px;width:110px;height:36px;font-size:13px">Submit</div>
</form>

<!-- footer -->
<footer class="footer"></footer>
<div class="brand" style="left:111px;top:3462px;font-size:24px"><span class="brand-mark"></span>Voltaro Works</div>
<p class="abs" style="left:111px;top:3530px;width:270px;color:#fff;font-size:14px;line-height:26px">Norvik Circuits A / S 's production department for electronics was closed down and sold in July 2001 .</p>
<div class="social" style="left:113px" aria-label="Social link"></div>
<div class="social" style="left:157px" aria-label="Social link"></div>
<div class="social" style="left:201px" aria-label="Social link"></div>
<div class="social" style="left:245px" aria-label="Social link"></div>

<div class="fhead" style="left:451px;top:3440px">Use Link</div>
<ul class="flist" style="left:453px;top:3467px"><li>Home</li><li>About</li><li>Services</li><li>Products</li><li>Contact</li></ul>
<div class="fhead" style="left:656px;top:3440px">Help Link</div>
<ul class="flist" style="left:657px;top:3467px"><li>Terms&amp;condtions</li><li>Privacy Policy</li><li>Support</li><li>Blog</li></ul>
<div class="fhead" style="left:879px;top:3438px">Contact Us</div>
<svg class="abs" style="left:872px;top:3470px" width="28" height="28" viewBox="0 0 28 28" fill="none" stroke="#fff" stroke-width="1.5"><circle cx="14" cy="14" r="13"/><path d="M10 8l3 3-2 2c1 2 2 3 4 4l2-2 3 3-2 2c-5 0-10-5-10-10z"/></svg>
<div class="abs" style="left:910px;top:3475px;color:#fff;font-size:15px">900 41 275</div>
<svg class="abs" style="left:872px;top:3516px" width="28" height="28" viewBox="0 0 28 28" fill="none" stroke="#fff" stroke-width="1.5"><circle cx="14" cy="14" r="13"/><rect x="8" y="10" width="12" height="9"/><path d="M8 10l6 5 6-5"/></svg>
<div class="abs" style="left:910px;top:3521px;color:#fff;font-size:15px">post@voltaroworks.no</div>
<svg class="abs" style="left:870px;top:3556px" width="28" height="28" viewBox="0 0 28 28" fill="none" stroke="#fff" stroke-width="1.5"><circle cx="14" cy="14" r="13"/><path d="M14 21s-5-5-5-9a5 5 0 0110 0c0 4-5 9-5 9z"/><circle cx="14" cy="12" r="1.8"/></svg>
<div class="abs" style="left:910px;top:3554px;color:#fff;font-size:15px;line-height:32px">Fjordbakken 12<br>4610 Sandvik Norway</div>
<div class="abs" style="left:111px;top:3683px;width:978px;height:1px;background:#555"></div>
<div class="abs" style="left:0;top:3703px;width:1200px;text-align:center;color:#fff;font-size:15px">©Copyrights voltaroworks | All Rights Reserved</div>

</body>
</html>
```